Skincare Clinic specializing in treating difficult skin conditions needs a web design

We want to restructure and rehash our current webdesigns. The current ones are dated and look very old fashioned also, they are not structured well.

The current websites need to get an uplift in look and become more classy and modern with navigation ease by structuring the information into ease of access

The current web address is
www.brellowderm.com.au and
www.velmarash.com.au

We also have international Partner website which is good and we need to better than them. So this website will act as a guide to better the new site
www.tenquil-drsorvan.com

But the new site should be more inclined towards a Blue colour or Aqua marine blue orientation and it needs to be Scientific giving authenticity to the medical industry we operate in.

Attached is a webdesign framework and architecture we would want to adopt. It is a schematic diagram and you can creatively adopt based on what you want to propose.

The website needs to be coded and Should be coded in WordPress such that it helps with SEO activity and google adwords pickup.

We will need the necessary pictures and we could provide them or agree to by them from the designers source.

Target Market(s)

Patients with Skin Disease and people interested to book consultation or buy products for their Skin condition

Industry/Entity Type

Clinic

Coding

Coded - Design and coding required

Number of Pages Required

5+ page

Font styles to use
Other font styles liked:
• Use a light font denoting class.

Requirements
Must have
• Should be modern, Easy to navigate, mobile friendly and coded in wordpress
• Blue colour and should look scientific and medicinal
Nice to have
• Classy and creative
Should not have
• No Green colour or herbal look

```html
<!DOCTYPE html>
<html lang="en">
<head>
<meta charset="utf-8">
<title>Brellowderm by Velmara Skin Clinic</title>
<link href="https://fonts.googleapis.com/css2?family=Open+Sans:wght@300;400;600;700&family=PT+Serif:wght@400&display=swap" rel="stylesheet">
<style>
:root{
  --blue:#17a3de;
  --teal:#6ccad2;
  --teal-light:#9fe1e6;
  --ink:#444;
  --ink-soft:#555;
  --grey-band:#777;
  --footer:#666;
  --white:#fff;
  --line:#e3e3e3;
}
*{box-sizing:border-box;margin:0;padding:0}
html,body{width:1200px;height:2171px;overflow:hidden;background:var(--white)}
body{position:relative;font-family:"Open Sans",Arial,sans-serif;color:var(--ink)}
.abs{position:absolute}
ul{list-style:none}

/* header */
.promo{left:100px;top:33px;width:552px;height:123px;border:1px solid #999;background:linear-gradient(90deg,#f4f1ee,#fff 60%,#f0ece8)}
.promo-products{left:6px;top:12px;width:100px;height:98px;background:linear-gradient(180deg,#e8dccd,#c9b7a2);border-radius:4px}
.promo-bottle{left:520px;top:12px;width:22px;height:98px;background:linear-gradient(90deg,#444,#bbb,#555);border-radius:3px}
.promo-title{left:123px;top:6px;font-family:"PT Serif",Georgia,serif;font-size:24px;line-height:25px;color:#333}
.promo-btn{left:125px;top:57px;width:138px;height:37px;background:#eee;border:1px solid #ddd;font-size:15px;text-align:center;line-height:35px;color:#333}
.promo-price{right:32px;top:70px;font-family:"PT Serif",Georgia,serif;text-align:right;font-size:16px;line-height:17px;color:#333}
.promo-price small{font-size:13px}
.social{left:892px;top:46px;display:flex;gap:8px}
.social span{width:30px;height:30px;border-radius:50%;background:#d5d5d5;display:block}
.brand{display:flex;align-items:center;gap:12px}
.brand-name{font-weight:600;color:var(--blue);line-height:1}
.brand-name b{display:block;font-weight:600;font-size:42px;letter-spacing:-1px}
.brand-name i{display:block;font-style:normal;font-size:19px;margin-top:2px}
.brand-dot{width:54px;height:54px;border-radius:50%;background:var(--blue);flex:none}
.brand-top{left:800px;top:86px}

/* nav */
.nav{left:0;top:178px;width:1200px;height:49px;background:var(--blue)}
.nav a{position:absolute;top:0;height:49px;line-height:49px;color:var(--white);font-size:15px;text-decoration:none;text-transform:uppercase}
.nav a.active{background:var(--teal);padding:0 16px;left:100px}
.nav .sep{position:absolute;top:15px;height:20px;border-left:1px dotted rgba(255,255,255,.6)}

/* hero */
.hero{left:0;top:227px;width:1200px;height:485px;background:radial-gradient(circle at 860px 230px,#e0b39b 0,#d9a78c 120px,#eef2f5 300px),linear-gradient(90deg,#eef1f4,#f9fafb)}
.hero-arrow{top:198px}
.hero-title{left:100px;top:222px;width:556px;height:94px;background:var(--white);font-weight:300;font-size:44px;color:var(--blue);line-height:94px;padding-left:20px}
.hero-caption{left:100px;top:330px;width:650px;height:61px;background:var(--grey-band);color:var(--white);font-family:Arial,sans-serif;font-size:14px;line-height:20px;padding:10px 20px}

/* services */
.services{left:0;top:712px;width:1200px;height:505px;background:var(--teal)}
.card{top:112px;width:275px;height:295px;border:1px solid rgba(255,255,255,.9)}
.card-badge{left:50%;top:-72px;width:100px;height:100px;margin-left:-50px;border-radius:50%;background:var(--teal);display:flex;align-items:center;justify-content:center}
.card-badge span{width:78px;height:78px;border-radius:50%;background:var(--white);border:10px solid var(--blue)}
.card-title{top:40px;width:100%;text-align:center;font-size:24px;font-weight:400;color:#3a3a3a}
.field{left:15px;width:241px;height:37px;background:var(--white);border:1px solid #ddd;font-size:14px;color:#aaa;padding:8px 13px}
.btn-book{left:38px;top:266px;width:184px;height:47px;background:var(--blue);color:var(--white);font-size:18px;text-align:center;line-height:47px}
.card-photo{left:16px;top:84px;width:241px;height:145px;border:4px solid var(--white)}
.btn-buy{left:42px;top:265px;width:193px;height:48px;background:var(--teal-light);border:1px solid var(--white);font-size:19px;text-align:center;line-height:46px;color:#333}

/* about */
.about{left:0;top:1217px;width:1200px;height:480px;background:linear-gradient(120deg,#eef0f4,#f7f3f0 40%,#f0e9e4 70%,#ece6e1)}
.kicker{font-size:21px;color:var(--blue);font-weight:400}
.heading{font-size:27px;font-weight:300;color:#333;letter-spacing:.5px}
.doctor{left:100px;top:126px;width:240px;height:354px;background:linear-gradient(180deg,#d9b596 0,#e9ecef 28%,#dfe3e8 70%,#6e7078 100%)}
.about-text{left:350px;top:140px;width:322px;font-size:14.5px;line-height:22px;color:#333}
.about-text strong{font-weight:600;color:#222}
.about-list{left:350px;top:310px;width:330px;font-size:13px;line-height:24.5px;color:#444}
.about-list li::before{content:"›";color:#999;margin-right:10px}
.divider{left:692px;top:28px;height:420px;border-left:1px solid #d6d6d6}
.case-nav{left:1064px;top:62px}
.case-img{top:115px;width:174px;height:136px;border-radius:4px}
.view-all{font-size:14px;font-weight:600;color:#333}
.case-text{left:717px;top:300px;width:370px;font-size:14.5px;line-height:22px;color:#333}

/* unique */
.kicker-b{font-size:21px;color:var(--blue)}
.step-num{width:42px;height:42px;border-radius:50%;color:var(--white);font-size:17px;text-align:center;line-height:42px}
.step-text{left:164px;width:500px;font-size:14.5px;line-height:22px;color:#333}
.step-rule{left:100px;top:1899px;width:560px;border-top:1px solid #eee}
.quote-brace{left:702px;top:1828px}
.client-photo{left:741px;top:1851px;width:80px;height:67px;border:2px solid var(--white);box-shadow:0 0 0 1px #ddd;background:linear-gradient(180deg,#3c2d28,#d6ab92 55%,#f3f3f3)}
.client-text{left:834px;top:1829px;width:270px;font-size:14.5px;line-height:22px;color:#444}

/* footer */
.footer{left:0;top:2070px;width:1200px;height:101px;background:var(--footer)}
.footer-links{left:100px;top:28px;font-size:13px;color:var(--white)}
.footer-links span{margin:0 8px}
.copyright{left:100px;top:55px;font-family:Arial,sans-serif;font-size:13px;color:var(--teal)}
.footer .brand-name{color:var(--white)}
.footer .brand-dot{background:var(--white)}
</style>
</head>
<body>

<header>
  <div class="promo abs">
    <div class="promo-products abs" role="img" aria-label="Skincare product range bottles"></div>
    <div class="promo-title abs">Transform Your Skin To A More<br>Youthful Appearance</div>
    <div class="promo-btn abs">Read More</div>
    <div class="promo-price abs">Lumera Peptide Lift<br><small>$12 (Save 52%)</small></div>
    <div class="promo-bottle abs" role="img" aria-label="Serum bottle"></div>
  </div>
  <div class="social abs" aria-label="Social links"><span></span><span></span><span></span><span></span></div>
  <div class="brand brand-top abs">
    <div class="brand-name"><b>brellowderm</b><i>by Velmara Skin Clinic</i></div>
    <span class="brand-dot"></span>
  </div>
</header>

<nav class="nav abs">
  <a class="active">Home</a>
  <a style="left:204px">About us</a><span class="sep" style="left:301px"></span>
  <a style="left:333px">Treatments</a><span class="sep" style="left:446px"></span>
  <a style="left:475px">Products</a><span class="sep" style="left:574px"></span>
  <a style="left:605px">Results</a><span class="sep" style="left:686px"></span>
  <a style="left:708px">Media</a><span class="sep" style="left:777px"></span>
  <a style="left:802px">Skin Coditions</a>
</nav>

<section class="hero abs" role="img" aria-label="Woman with glowing skin beside a splash of water">
  <svg class="hero-arrow abs" style="left:46px" width="24" height="46" viewBox="0 0 24 46"><path d="M22 2 2 23l20 21" fill="none" stroke="#aab" stroke-width="2"/></svg>
  <svg class="hero-arrow abs" style="left:1124px" width="24" height="46" viewBox="0 0 24 46"><path d="M2 2l20 21L2 44" fill="none" stroke="var(--blue)" stroke-width="2"/></svg>
  <h1 class="hero-title abs">SPECIAL CARE SOLUTIONS</h1>
  <p class="hero-caption abs">simply dummy text of the printing and typesetting industry. Lorem Ipsum has been the industry's standard dummy text ever since the 1500s, when an unknown printer.</p>
</section>

<section class="services abs">
  <div class="card abs" style="left:142px">
    <div class="card-badge abs"><span></span></div>
    <h2 class="card-title abs">For Consultation</h2>
    <div class="field abs" style="top:81px">name</div>
    <div class="field abs" style="top:126px">address</div>
    <div class="field abs" style="top:171px;height:74px">tell us about your problem</div>
    <div class="btn-book abs">BOOK ONLINE</div>
  </div>
  <div class="card abs" style="left:454px">
    <div class="card-badge abs"><span></span></div>
    <h2 class="card-title abs">Online Products</h2>
    <div class="card-photo abs" role="img" aria-label="Woman rinsing her face with water" style="background:linear-gradient(180deg,#d9c8bd,#c9a58f 50%,#e6e1dc)"></div>
    <div class="btn-buy abs">Purchase Products</div>
  </div>
  <div class="card abs" style="left:764px">
    <div class="card-badge abs"><span></span></div>
    <h2 class="card-title abs">Online Products</h2>
    <div class="card-photo abs" role="img" aria-label="Doctor examining a child with his mother" style="background:linear-gradient(90deg,#e8edf0,#c9b2a4 50%,#e7e2de)"></div>
    <div class="btn-buy abs">Purchase Products</div>
  </div>
</section>

<section class="about abs">
  <p class="kicker abs" style="left:130px;top:28px">About</p>
  <h2 class="heading abs" style="left:130px;top:57px">Dr. Sorvan Keller</h2>
  <div class="doctor abs" role="img" aria-label="Smiling doctor in white coat holding a clipboard"></div>
  <p class="about-text abs"><strong>Simply dummy text of the printing and typesetting industry. Lorem Ipsum has been</strong> the industry's standard dummy text ever since the 1500s, when an unknown printer took a galley of type and scrambled it to make a type specimen book. It has survived not only five centuries.It was popularised in the 1960s with the release of Letraset.</p>
  <ul class="about-list abs">
    <li>Donec vulputate et nisl a scelerisque .</li>
    <li>Nullam eros arcu, imperdiet eget magna sit amet.</li>
    <li>Curabitur metus nunc, varius eu velit et, lobortis .</li>
    <li>Morbi mi justo, interdum sit amet orci nec..</li>
    <li>Donec vulputate et nisl a scelerisque .</li>
    <li>Nullam eros arcu, imperdiet eget magna sit amet.</li>
  </ul>
  <div class="divider abs"></div>
  <p class="kicker abs" style="left:717px;top:28px">View</p>
  <h2 class="heading abs" style="left:717px;top:57px">Case Studies</h2>
  <svg class="case-nav abs" width="24" height="14" viewBox="0 0 24 14"><path d="M8 2 3 7l5 5" fill="none" stroke="#888" stroke-width="2"/><path d="M15 2l5 5-5 5" fill="none" stroke="#111" stroke-width="2.4"/></svg>
  <div class="case-img abs" style="left:717px;background:linear-gradient(90deg,#c99a7a,#dcb090 50%,#c7926f)" role="img" aria-label="Before and after facial skin treatment"></div>
  <div class="case-img abs" style="left:913px;background:linear-gradient(90deg,#c98c78,#e1b7a3 55%,#eec6b1)" role="img" aria-label="Before and after acne treatment"></div>
  <p class="view-all abs" style="left:1025px;top:272px">View All</p>
  <div class="case-text abs">
    <p>Simply dummy text of the printing and typesetting industry. Lorem Ipsum has been the industry's standard dummy text ever since the 1500s..</p>
    <p style="margin-top:22px">It has survived not only five centuries.It was popularised in the 1960s with the release of Letraset.</p>
  </div>
</section>

<section class="unique">
  <p class="kicker-b abs" style="left:100px;top:1740px">What's Unique</p>
  <h2 class="heading abs" style="left:100px;top:1772px">About Our Treatment Protcols</h2>
  <div class="step-num abs" style="left:101px;top:1825px;background:var(--blue)">1</div>
  <p class="step-text abs" style="top:1824px">Simply dummy text of the printing and typesetting industry. Lorem Ipsum has been the industry's.It has survived not only five centuries.It was popularised in the 1960s with the release of Letraset.</p>
  <div class="step-rule abs"></div>
  <div class="step-num abs" style="left:101px;top:1917px;background:var(--teal)">2</div>
  <p class="step-text abs" style="top:1915px">Simply dummy text of the printing and typesetting industry. Lorem Ipsum has been the industry's.It has survived not only five centuries.It was popularised in the 1960s with the release of Letraset.</p>
  <p class="view-all abs" style="left:100px;top:1983px">View All</p>

  <p class="kicker-b abs" style="left:722px;top:1747px">Client's</p>
  <h2 class="heading abs" style="left:722px;top:1779px">Testimonial</h2>
  <svg class="quote-brace abs" width="24" height="110" viewBox="0 0 24 110"><path d="M20 2C10 2 10 8 10 20v22c0 8-4 12-8 13 4 1 8 5 8 13v22c0 12 0 18 10 18" fill="none" stroke="#ccc" stroke-width="3"/></svg>
  <div class="client-photo abs" role="img" aria-label="Portrait of a smiling client"></div>
  <p class="client-text abs">Simply dummy text of the printing and typesetting industry. Lorem Ipsum has been the industry's standard dummy text ever since the 1500s, when an unknown printer took a galley.</p>
  <p class="view-all abs" style="left:740px;top:1970px">View All</p>
</section>

<footer class="footer abs">
  <p class="footer-links abs">Home<span>|</span>About Us<span>|</span>Treatments<span>|</span>Our services<span>|</span>Our Products</p>
  <p class="copyright abs">© 2015 Brellowderm. All rights reserved.</p>
  <div class="brand abs" style="left:800px;top:14px">
    <div class="brand-name"><b>brellowderm</b><i>by Velmara Skin Clinic</i></div>
    <span class="brand-dot"></span>
  </div>
</footer>

</body>
</html>
```